Brovelline International is looking for web design

I have a website that I made myself and I wanted to have a more professional design. go to my website www.BrovellinePX.example and you will see what it is all about. My website was created with Weebly. we like to focus on that we have an earth friendly product. we offer a natural alternative to asphalt or concrete .

Target Market(s)

Landscape Archtects, Home Improvement , designers, parks and recreation

Industry/Entity Type

It Professional

Coding

Coded - Design and coding required

Number of Pages Required

5+ page

Requirements
Must have
• Landing page,
• Products Page contact us page

```html
<!DOCTYPE html>
<html lang="en">
<head>
<meta charset="utf-8">
<title>Contact – Brovelline International</title>
<link rel="stylesheet" href="https://fonts.googleapis.com/css2?family=Open+Sans:wght@400;600;700&display=swap">
<style>
:root{
  --green:#6aaa1e;
  --text:#222;
  --muted:#555;
  --nav:#4a4a4a;
  --border:#b9b9b9;
  --placeholder:#9a9a9a;
  --footer:#dedede;
  --skyline:#d2d2d2;
  --red:#d0021b;
}
*{box-sizing:border-box;margin:0;padding:0}
html,body{width:1200px;height:1078px;overflow:hidden;background:#fff}
body{font-family:"Open Sans",sans-serif;color:var(--text);position:relative}
.abs{position:absolute}
.brand{display:flex;align-items:center;gap:8px;font-size:15px;font-weight:700;color:var(--green);letter-spacing:.5px;white-space:nowrap}
.brand .dot{width:26px;height:26px;border-radius:50%;background:var(--green)}
.nav{top:29px;left:595px;font-size:13.5px;color:var(--nav)}
.nav a{position:absolute;white-space:nowrap;text-decoration:none;color:inherit}
.nav a.active{color:var(--green)}
.hero{top:75px;left:0;width:1200px;height:157px;background:linear-gradient(180deg,#8a8f88 0%,#9b8150 25%,#a27e3d 60%,#6e5224 100%)}
.hero h1{position:absolute;left:0;right:0;top:52px;text-align:center;color:#fff;font-size:45px;font-weight:600;letter-spacing:1px}
.crumb{top:248px;left:106px;font-size:11px;color:#6b5433}
.intro{top:308px;left:107px;font-size:16.5px;font-weight:700;white-space:nowrap}
.sub{top:341px;left:107px;font-size:13px}
.label{font-size:13px;color:var(--text)}
.label em{color:var(--red);font-style:normal}
.field{border:1px solid var(--border);border-radius:2px;background:#fff;font-size:13px;color:var(--placeholder);padding:8px 14px}
.slash{font-size:12px;color:#777}
.submit{left:105px;top:840px;width:93px;height:34px;background:var(--green);color:#fff;font-size:13.5px;border-radius:2px;display:flex;align-items:center;justify-content:center}
.info{display:flex;align-items:center;gap:10px;color:var(--text);white-space:nowrap}
.info svg{width:14px;height:14px}
.rule{left:668px;top:529px;width:425px;height:1px;background:#cfcfcf}
.map{left:668px;top:573px;width:425px;height:301px;border:1px solid #bbb;background:linear-gradient(135deg,#9cc3e6 0%,#d9d6cc 45%,#cfc9bb 70%,#a8c8e4 100%)}
.footer{left:0;top:921px;width:1200px;height:157px;background:var(--footer);overflow:hidden}
.footer .backdrop{position:absolute;left:0;bottom:0;width:1200px;height:120px;background:linear-gradient(180deg,rgba(210,210,210,0) 0%,var(--skyline) 100%)}
.footer .copy{position:absolute;top:72px;left:0;right:0;text-align:center;font-size:11.5px}
.social{position:absolute;top:101px;width:23px;height:23px;border-radius:50%;background:#2b2b2b}
</style>
</head>
<body>
<header>
  <div class="abs brand" style="top:24px;left:106px"><span class="dot"></span>BROVELLINE INTERNATIONAL</div>
  <nav class="abs nav">
    <a style="left:0">Home</a>
    <a style="left:55px">Products</a>
    <a style="left:129px">Ask The Experts</a>
    <a style="left:245px">Distributors</a>
    <a class="active" style="left:337px">Contact Us</a>
    <a style="left:422px">Media</a>
  </nav>
  <svg class="abs" style="top:30px;left:1075px" width="16" height="16" viewBox="0 0 16 16"><circle cx="6.5" cy="6.5" r="4.8" fill="none" stroke="#4a4a4a" stroke-width="2.2"/><line x1="10" y1="10" x2="14.5" y2="14.5" stroke="#4a4a4a" stroke-width="2.6" stroke-linecap="round"/></svg>
</header>

<section class="abs hero" role="img" aria-label="Photo of a message bottle lying on a sandy beach"><h1>CONTACT</h1></section>

<div class="abs crumb">Home &gt; Contact</div>
<h2 class="abs intro">Give us a call or send us a message using the form below.&nbsp; We are always happy to help</h2>
<p class="abs sub">We Would Love To Hear From You</p>

<form>
  <div class="abs label" style="top:409px;left:106px">Name<em>*</em></div>
  <div class="abs field" style="top:436px;left:105px;width:204px;height:33px">First</div>
  <div class="abs field" style="top:436px;left:327px;width:203px;height:33px">Last</div>
  <div class="abs label" style="top:483px;left:107px">Company Name</div>
  <div class="abs field" style="top:510px;left:105px;width:425px;height:34px">Type your company Name</div>
  <div class="abs label" style="top:558px;left:107px">Phone Number</div>
  <div class="abs field" style="top:584px;left:105px;width:84px;height:33px"></div>
  <span class="abs slash" style="top:592px;left:206px">/</span>
  <div class="abs field" style="top:584px;left:230px;width:93px;height:33px"></div>
  <span class="abs slash" style="top:592px;left:341px">/</span>
  <div class="abs field" style="top:584px;left:365px;width:165px;height:33px"></div>
  <div class="abs label" style="top:632px;left:107px">Email<em>*</em></div>
  <div class="abs field" style="top:658px;left:105px;width:425px;height:34px">Type your email address</div>
  <div class="abs label" style="top:707px;left:108px">Comments or Questions<em>*</em></div>
  <div class="abs field" style="top:735px;left:105px;width:425px;height:87px">Type your comment or Question here</div>
  <div class="abs submit">Submit</div>
</form>

<aside>
  <div class="abs info" style="top:433px;left:670px;font-size:17px">
    <svg viewBox="0 0 14 14"><path d="M7 1a4.2 4.2 0 0 0-4.2 4.2C2.8 8.4 7 13 7 13s4.2-4.6 4.2-7.8A4.2 4.2 0 0 0 7 1z" fill="var(--green)"/><circle cx="7" cy="5.2" r="1.6" fill="#fff"/></svg>(555) 014-2286</div>
  <div class="abs info" style="top:465px;left:670px;font-size:13px">
    <svg viewBox="0 0 14 14"><rect x="1" y="3" width="12" height="9" fill="var(--green)"/><path d="M1 3l6 5 6-5" fill="none" stroke="#fff" stroke-width="1.2"/></svg>info@brovelline.example</div>
  <div class="abs info" style="top:493px;left:670px;font-size:13px">
    <svg viewBox="0 0 14 14" fill="none" stroke="var(--green)" stroke-width="1.3"><circle cx="7" cy="7" r="6"/><ellipse cx="7" cy="7" rx="2.6" ry="6"/><line x1="1" y1="7" x2="13" y2="7"/><line x1="2" y1="4" x2="12" y2="4"/><line x1="2" y1="10" x2="12" y2="10"/></svg>www.brovellinepx.example</div>
  <div class="abs rule"></div>
  <div class="abs map" role="img" aria-label="Map showing the office location"></div>
</aside>

<footer class="abs footer">
  <div class="backdrop" role="img" aria-label="Faint city skyline silhouette behind the footer"></div>
  <div class="abs brand" style="top:30px;left:524px;font-size:13px"><span class="dot" style="width:22px;height:22px"></span>BROVELLINE INTERNATIONAL</div>
  <p class="copy">© Copyright 2016 Brovelline International, All rights reserved <b>(555) 019-3417</b></p>
  <span class="social" style="left:559px"></span>
  <span class="social" style="left:589px"></span>
  <span class="social" style="left:620px"></span>
</footer>
</body>
</html>
```